Business Card for my building company

I would like the card to make a statement, so as soon as you see the card you think "wow nice card' and then read the details on the card its self. Also i would like to be able to put in the detail for the MUST HAVES so please Crete a box that i can alter depending on who in my business needs the cards. Thank you

Target Market(s)

Any one looking to build a house/ townhouse or duplex

Industry/Entity Type

Home Builder

Contact Information for Business Card

I would like the card to have the logo on the card and the must haves

Font styles to use
Sans Serif

Requirements
Must have
• Name
• Phone Number
• Email Address
• Website
• Licence Number
• Abn

```html
<!DOCTYPE html>
<html lang="en">
<head>
<meta charset="UTF-8">
<title>Coastline Builders — Business Card</title>
<link rel="stylesheet" href="https://fonts.googleapis.com/css2?family=Questrial&display=swap">
<style>
  :root {
    --page-bg: #f2f2f2;
    --card-bg: #ffffff;
    --band: #3b3e40;
    --frame: #45484b;
    --text: #1a1a1a;
    --red: #c4262e;
    --blue: #17a6e6;
    --green: #0ea44a;
    --pink: #e2147a;
    --yellow: #eeac1f;
    --teal: #129db0;
    --purple: #5d2b90;
    --brick-dark: #2a1d15;
    --brick-mid: #5a3f2c;
    --wood: #6b4527;
  }
  * { margin: 0; padding: 0; box-sizing: border-box; }
  html, body {
    width: 1200px;
    height: 2397px;
    overflow: hidden;
    background: var(--page-bg);
  }
  .business-card {
    position: absolute;
    left: 50px;
    top: 876px;
    width: 1100px;
    height: 644px;
    background: var(--card-bg);
    border: 2px solid #222;
    overflow: hidden;
    font-family: "Questrial", sans-serif;
    color: var(--text);
  }
  .card-lines {
    position: absolute;
    inset: 0;
    width: 100%;
    height: 100%;
  }
  .card-lines polyline, .card-lines line {
    fill: none;
    stroke-width: 4;
    stroke-linejoin: miter;
  }
  .band {
    position: absolute;
    left: 0;
    width: 100%;
    height: 40px;
    background: var(--band);
  }
  .band--top { top: 0; }
  .band--bottom { bottom: 0; }
  .detail-list {
    position: absolute;
    left: 40px;
    top: 108px;
    list-style: none;
    font-size: 25px;
    line-height: 79.3px;
    letter-spacing: 0.3px;
  }
  .logo-box {
    position: absolute;
    left: 733px;
    top: 227px;
    width: 230px;
    height: 191px;
    border: 7px solid var(--frame);
    background: var(--frame);
  }
  .logo-backdrop {
    position: absolute;
    inset: 0;
    background: linear-gradient(180deg, var(--brick-mid) 0%, var(--brick-dark) 55%, var(--wood) 100%);
  }
  .company-name {
    position: absolute;
    inset: 0;
    display: flex;
    flex-direction: column;
    align-items: center;
    justify-content: center;
    color: #ffffff;
    font-size: 27px;
    line-height: 1.15;
    text-align: center;
  }
</style>
</head>
<body>
  <div class="business-card">
    <svg class="card-lines" viewBox="0 0 716 419" preserveAspectRatio="none" aria-hidden="true">
      <!-- left routes -->
      <polyline points="0,54 437,54 505,148" stroke="var(--red)"/>
      <polyline points="0,106 437,106 482,150" stroke="var(--blue)"/>
      <polyline points="0,157 437,157 477,172" stroke="var(--green)"/>
      <line x1="0" y1="209" x2="716" y2="209" stroke="var(--pink)"/>
      <polyline points="0,261 437,261 477,245" stroke="var(--yellow)"/>
      <polyline points="0,313 437,313 482,270" stroke="var(--teal)"/>
      <polyline points="0,364 437,364 505,272" stroke="var(--purple)"/>
      <!-- right routes -->
      <line x1="610" y1="150" x2="716" y2="64" stroke="var(--red)"/>
      <line x1="625" y1="162" x2="716" y2="106" stroke="var(--blue)"/>
      <line x1="627" y1="185" x2="716" y2="157" stroke="var(--green)"/>
      <line x1="627" y1="248" x2="716" y2="275" stroke="var(--yellow)"/>
      <line x1="625" y1="262" x2="716" y2="328" stroke="var(--teal)"/>
      <line x1="610" y1="272" x2="716" y2="364" stroke="var(--purple)"/>
    </svg>

    <div class="band band--top"></div>
    <div class="band band--bottom"></div>

    <ul class="detail-list">
      <li>Name:</li>
      <li>Phone Number:</li>
      <li>Email Address:</li>
      <li>Website:</li>
      <li>Licence Number:</li>
      <li>Abn:</li>
    </ul>

    <div class="logo-box">
      <div class="logo-backdrop" role="img" aria-label="Photo of a brick wall above a timber floor"></div>
      <div class="company-name"><span>Coastline</span><span>Builders</span></div>
    </div>
  </div>
</body>
</html>
```